Bref créative
Saltmarsh Restaurant
Truly Island-Made
Simple
#41 Estate Coralind
(at the Harbor Bluff Cottages)
Christiansted, VI 00820
Saltmarsh_Restaurant@bayvistamail.com
www.saltmarshvi-example.com
* Free Wi-fi
* Special events venue-mediations, meetings, fund raisers, wedding receptions, catering, private parties, you name it we can host it !!
* Superior customer service
* Delicious cuisine
please use this logo

```html
<!DOCTYPE html>
<html lang="en">
<head>
<meta charset="utf-8">
<title>Saltmarsh Restaurant – Business Cards</title>
<link href="https://fonts.googleapis.com/css2?family=Arimo:wght@400;700&display=swap" rel="stylesheet">
<style>
  :root {
    --stage: #8c8c8c;
    --paper: #ffffff;
    --ink: #2b2b2b;
    --ink-soft: #5a5a5a;
    --night: #161616;
    --night-edge: #2c2c2c;
    --sand: #d8c79c;
    --sand-deep: #c2ae7c;
    --aqua: #bfe3df;
    --aqua-deep: #9fd0cb;
    --gold: #c8a94e;
    --teal-mark: #5b9b97;
    --rule: #b9b9b9;
  }
  * { box-sizing: border-box; margin: 0; padding: 0; }
  html, body { width: 1200px; height: 744px; overflow: hidden; }
  body {
    background: var(--stage);
    font-family: "Arimo", Arial, sans-serif;
    position: relative;
  }
  .card {
    position: absolute;
    width: 480px;
    height: 276px;
    border-radius: 14px;
    overflow: hidden;
    box-shadow: 0 6px 18px rgba(0,0,0,.35);
  }
  .card--light { background: var(--paper); color: var(--ink); }
  .card--dark { background: var(--night); color: #e9e9e9; border: 1px solid var(--night-edge); }
  .pos-front-light { left: 90px; top: 80px; }
  .pos-front-dark { left: 630px; top: 80px; }
  .pos-back-light { left: 90px; top: 396px; }
  .pos-back-dark { left: 630px; top: 396px; }

  .header {
    height: 74px;
    padding: 12px 22px 0;
  }
  .card--light .header { background: linear-gradient(var(--sand) 0 62%, var(--sand-deep) 62% 100%); }
  .card--dark .header { background: linear-gradient(var(--aqua) 0 62%, var(--aqua-deep) 62% 100%); }
  .header__name {
    font-weight: 700;
    font-size: 24px;
    color: var(--ink);
    letter-spacing: .2px;
  }
  .header__tagline {
    font-weight: 700;
    font-size: 13px;
    color: var(--ink);
    margin-top: 14px;
  }
  .header-rule { height: 3px; background: var(--rule); }
  .card--dark .header-rule { background: #cfcfcf; }

  .front-body {
    display: flex;
    height: 199px;
  }
  .brand {
    width: 218px;
    display: flex;
    align-items: center;
    justify-content: center;
    gap: 8px;
    border-right: 1px solid var(--rule);
    margin: 18px 0;
  }
  .card--dark .brand { border-right-color: #555; }
  .brand__dot {
    width: 14px; height: 14px; border-radius: 50%;
    background: var(--teal-mark);
  }
  .brand__name {
    font-size: 30px;
    font-weight: 400;
    color: var(--teal-mark);
  }
  .card--dark .brand__name { color: #e6e6e6; }
  .card--dark .brand__dot { background: var(--aqua-deep); }

  .contact {
    list-style: none;
    padding: 28px 0 0 14px;
    font-size: 9.5px;
    line-height: 1.35;
  }
  .contact li { display: flex; gap: 7px; margin-bottom: 7px; }
  .contact svg { flex: none; width: 11px; height: 11px; margin-top: 1px; }
  .card--light .contact { color: var(--ink-soft); }
  .card--dark .contact { color: #d4d4d4; }

  .services {
    list-style: none;
    padding: 28px 28px 0;
    font-size: 9.5px;
    line-height: 1.4;
    width: 360px;
  }
  .card--light .services { color: var(--ink-soft); }
  .card--dark .services { color: #d0d0d0; }

  .back-mark {
    position: absolute;
    right: 30px;
    bottom: 48px;
    font-size: 28px;
    color: var(--gold);
  }
  .back-url {
    position: absolute;
    right: 22px;
    bottom: 16px;
    font-size: 12px;
  }
  .card--light .back-url { color: var(--ink); }
  .card--dark .back-url { color: #f0f0f0; }
</style>
</head>
<body>

<svg width="0" height="0" style="position:absolute">
  <defs>
    <symbol id="icon-pin" viewBox="0 0 12 12"><circle cx="6" cy="6" r="5.5" fill="currentColor" opacity=".25"/><path d="M6 2.5a2.2 2.2 0 0 0-2.2 2.2C3.8 6.4 6 9.5 6 9.5s2.2-3.1 2.2-4.8A2.2 2.2 0 0 0 6 2.5z" fill="currentColor"/></symbol>
    <symbol id="icon-phone" viewBox="0 0 12 12"><circle cx="6" cy="6" r="5.5" fill="currentColor" opacity=".25"/><path d="M4 3h1.2l.6 1.5-.8.6a4.5 4.5 0 0 0 1.9 1.9l.6-.8L9 6.8V8a1 1 0 0 1-1 1A5 5 0 0 1 3 4a1 1 0 0 1 1-1z" fill="currentColor"/></symbol>
    <symbol id="icon-mail" viewBox="0 0 12 12"><circle cx="6" cy="6" r="5.5" fill="currentColor" opacity=".25"/><rect x="3" y="4" width="6" height="4.2" fill="none" stroke="currentColor" stroke-width=".9"/><path d="M3 4l3 2.3L9 4" fill="none" stroke="currentColor" stroke-width=".9"/></symbol>
    <symbol id="icon-web" viewBox="0 0 12 12"><circle cx="6" cy="6" r="5.5" fill="currentColor" opacity=".25"/><circle cx="6" cy="6" r="3" fill="none" stroke="currentColor" stroke-width=".9"/><path d="M3 6h6M6 3c-1.4 1.6-1.4 4.4 0 6M6 3c1.4 1.6 1.4 4.4 0 6" fill="none" stroke="currentColor" stroke-width=".7"/></symbol>
  </defs>
</svg>

<!-- Front, light -->
<section class="card card--light pos-front-light">
  <header class="header">
    <h1 class="header__name">Saltmarsh Restaurant</h1>
    <p class="header__tagline">Truly Island-Made</p>
  </header>
  <div class="header-rule"></div>
  <div class="front-body">
    <div class="brand"><span class="brand__dot"></span><span class="brand__name">Saltmarsh</span></div>
    <ul class="contact">
      <li><svg><use href="#icon-pin"/></svg><span>#41 Estate Coralind<br>(at the Harbor Bluff Cottages)<br>Christiansted, VI 00820</span></li>
      <li><svg><use href="#icon-phone"/></svg><span>340-555-0142</span></li>
      <li><svg><use href="#icon-phone"/></svg><span>340-555-0178/ 340-555-0193</span></li>
      <li><svg><use href="#icon-mail"/></svg><span>Saltmarsh_Restaurant@bayvistamail.com</span></li>
      <li><svg><use href="#icon-web"/></svg><span>www.saltmarshvi-example.com</span></li>
    </ul>
  </div>
</section>

<!-- Front, dark -->
<section class="card card--dark pos-front-dark">
  <header class="header">
    <h2 class="header__name">Saltmarsh Restaurant</h2>
    <p class="header__tagline">Truly Island-Made</p>
  </header>
  <div class="header-rule"></div>
  <div class="front-body">
    <div class="brand"><span class="brand__dot"></span><span class="brand__name">Saltmarsh</span></div>
    <ul class="contact">
      <li><svg><use href="#icon-pin"/></svg><span>#41 Estate Coralind<br>(at the Harbor Bluff Cottages)<br>Christiansted, VI 00820</span></li>
      <li><svg><use href="#icon-phone"/></svg><span>340-555-0142</span></li>
      <li><svg><use href="#icon-phone"/></svg><span>340-555-0178/ 340-555-0193</span></li>
      <li><svg><use href="#icon-mail"/></svg><span>Saltmarsh_Restaurant@bayvistamail.com</span></li>
      <li><svg><use href="#icon-web"/></svg><span>www.saltmarshvi-example.com</span></li>
    </ul>
  </div>
</section>

<!-- Back, light -->
<section class="card card--light pos-back-light">
  <ul class="services">
    <li>* Free Wi-fi</li>
    <li>* Special events venue-mediations, meetings, fund raisers, wedding receptions, catering, private parties, you name it we can host it !!</li>
    <li>* Superior customer service</li>
    <li>* Delicious cuisine</li>
  </ul>
  <span class="back-mark">Saltmarsh</span>
  <p class="back-url">www.saltmarshvi-example.com</p>
</section>

<!-- Back, dark -->
<section class="card card--dark pos-back-dark">
  <ul class="services">
    <li>* Free Wi-fi</li>
    <li>* Special events venue-mediations, meetings, fund raisers, wedding receptions, catering, private parties, you name it we can host it !!</li>
    <li>* Superior customer service</li>
    <li>* Delicious cuisine</li>
  </ul>
  <span class="back-mark">Saltmarsh</span>
  <p class="back-url">www.saltmarshvi-example.com</p>
</section>

</body>
</html>
```